Nestlyo Business Card Project showing the logo and a vonka image on the rear

Design a whacky but professional business card, the logo is for the front and the Vonka image is for the rear. Happy to consider other open source Vonka Images if the designer wants to select one from the web. Nestlyo is a competitor to KPX.com.au and Plotfield.com.au and is based around every property in Australia

Business

Name, Title, Email, Web, Phone Number

• avenir

• Image on Back logo on front
• Happy to consider other images on rear, preftably Oscar Vonka. Image supplied I own, we can use open source other Vonka Images

```html
<!DOCTYPE html>
<html lang="en">
<head>
<meta charset="utf-8">
<title>Nestlyo Business Card</title>
<link rel="stylesheet" href="https://fonts.googleapis.com/css2?family=Lexend:wght@500;600&family=Roboto:wght@400&display=swap">
<style>
  :root {
    --stage: #262626;
    --card-white: #f1f1f1;
    --card-shade: #e6e6e6;
    --brand-orange: #ee8a12;
    --ink: #151515;
    --text: #1e1e1e;
    --sky-day: #f18a12;
    --sky-night: #3a3c3f;
  }
  * { margin: 0; padding: 0; box-sizing: border-box; }
  html, body { width: 1200px; height: 1138px; overflow: hidden; background: var(--stage); }
  .stage { position: relative; width: 1200px; height: 1138px; }

  .card { position: absolute; border-radius: 14px; overflow: hidden; }

  .card-back { left: 274px; top: 185px; width: 623px; height: 376px; }
  .artwork {
    width: 100%; height: 100%;
    background: linear-gradient(90deg, var(--sky-day) 0%, #e9a23a 40%, #c96aa5 55%, #5a8fb8 75%, var(--sky-night) 100%);
  }

  .card-front {
    left: 276px; top: 607px; width: 618px; height: 375px;
    background: linear-gradient(180deg, var(--card-white) 0%, var(--card-shade) 100%);
    font-family: "Roboto", sans-serif; color: var(--text);
  }

  .brand { position: absolute; left: 46px; top: 140px; display: flex; align-items: center; gap: 20px; }
  .brand-mark { width: 58px; height: 58px; background: var(--brand-orange); }
  .brand-name { font-family: "Lexend", sans-serif; font-weight: 600; font-size: 54px; line-height: 1; color: var(--ink); letter-spacing: 0.3px; }

  .person { position: absolute; left: 381px; top: 82px; }
  .person-name { font-family: "Lexend", sans-serif; font-weight: 600; font-size: 24px; color: var(--brand-orange); line-height: 1.1; }
  .person-title { font-size: 16px; margin-top: 4px; }

  .contacts { position: absolute; left: 381px; top: 158px; list-style: none; }
  .contacts li { display: flex; align-items: center; height: 23.5px; font-size: 16px; }
  .contacts svg { width: 14px; height: 14px; margin-left: 2px; margin-right: 18px; flex: none; }
  .accent { color: var(--brand-orange); }

  .address { position: absolute; left: 381px; top: 236px; font-size: 16px; line-height: 20px; }

  .base-strip { position: absolute; left: 0; bottom: 0; width: 280px; height: 16px; background: var(--ink); }
  .tagline-band {
    position: absolute; right: 0; bottom: 0; width: 354px; height: 46px;
    background: var(--brand-orange);
    clip-path: polygon(20px 0, 100% 0, 100% 100%, 0 100%);
    display: flex; align-items: center; justify-content: center;
    padding-left: 20px;
    color: #fff; font-size: 16px;
  }
</style>
</head>
<body>
<main class="stage">
  <section class="card card-back">
    <div class="artwork" role="img" aria-label="Colourful pop-art cityscape of cartoon buildings and a train, orange day sky on the left and dark night sky on the right"></div>
  </section>

  <section class="card card-front">
    <div class="brand">
      <span class="brand-mark"></span>
      <span class="brand-name">Nestlyo</span>
    </div>

    <div class="person">
      <p class="person-name">Miles Garrow</p>
      <p class="person-title">Founder &amp; CEO</p>
    </div>

    <ul class="contacts">
      <li>
        <svg viewBox="0 0 16 16" aria-hidden="true"><circle cx="8" cy="8" r="7" fill="none" stroke="var(--brand-orange)" stroke-width="1.4"/><path d="M5.5 4.5l1.5 1.7-1 1c.6 1.3 1.5 2.2 2.8 2.8l1-1 1.7 1.5-1 1.2c-2.8-.3-5.3-2.8-5.6-5.6z" fill="var(--brand-orange)"/></svg>
        (02) 5550 1846
      </li>
      <li>
        <svg viewBox="0 0 16 16" aria-hidden="true"><rect x="1" y="3" width="14" height="10" fill="var(--brand-orange)"/><path d="M1 3l7 6 7-6" fill="none" stroke="#fff" stroke-width="1.2"/></svg>
        garrow@nestlyo.com
      </li>
      <li>
        <svg viewBox="0 0 16 16" aria-hidden="true"><circle cx="8" cy="8" r="7" fill="var(--brand-orange)"/><path d="M1 8h14M8 1v14M8 1c-3 3-3 11 0 14M8 1c3 3 3 11 0 14" fill="none" stroke="#fff" stroke-width="0.9"/></svg>
        <span>www.<span class="accent">nestlyo</span>.com</span>
      </li>
    </ul>

    <p class="address">Level 7, 48 Harbour Lane,<br>Sydney 2000, Australia</p>

    <div class="base-strip"></div>
    <div class="tagline-band">Buying, Selling and Research</div>
  </section>
</main>
</body>
</html>
```